Webshop for furniture and lamps

We need a design for a web shop with APP that should have two options:
1-Webshop in general which should attract to private customer in general and
2-Website that is meant to attract big customers as hotels and restaurants who would have their own customerize login.

That's the idea behind the shop.

It should be diveded into 4 parts
vintage furniture
rattan set outdoor and indoor
lamps and
wooden wall decor

The name of the shop is brisa novelta!

Please kindly make me an offer.

Reason: Dear designers, so far there hasn't been a design that really matched. Look up German web sites like www.fernblick-art.de or www.holzkante17.de... Haven't been convinced by designs! Sorry folks. Please submit some new ones. Kind regards Ned

```html
<!DOCTYPE html>
<html lang="en">
<head>
<meta charset="utf-8">
<title>Brisa Novelta – Furniture &amp; Lamps</title>
<link rel="stylesheet" href="https://fonts.googleapis.com/css2?family=Open+Sans:wght@400;600;700;800&display=swap">
<style>
:root{
  --red:#d13a30;
  --dark:#3b3735;
  --darker:#2d2a28;
  --mid:#4a4644;
  --text:#333;
  --muted:#8a8a8a;
  --line:#d9d9d9;
  --btn:#b9b2a0;
  --orange:#ef8a16;
  --star:#f2b01e;
  --white:#fff;
}
*{box-sizing:border-box;margin:0;padding:0}
html,body{width:1200px;height:2694px;overflow:hidden}
body{font-family:"Open Sans",Arial,sans-serif;color:var(--text);background:var(--white);font-size:12px;position:relative}
a{color:inherit;text-decoration:none}

.topbar{height:50px;background:var(--dark);color:#e8e4e0;display:flex;align-items:center;justify-content:space-between;padding:0 92px;font-size:13px}
.topbar nav{display:flex;gap:34px}

.header{height:118px;display:flex;align-items:center;justify-content:space-between;padding:0 92px}
.logo{display:flex;align-items:center;gap:14px;font-weight:800;font-size:34px;color:var(--red);letter-spacing:-.5px}
.logo-mark{width:66px;height:40px;background:var(--dark)}
.mainnav{display:flex;gap:20px;font-size:13px;font-weight:700;color:var(--dark);align-items:center}
.mainnav .sep{width:1px;height:20px;background:var(--line)}

.hero{margin:0 92px;height:312px;display:flex}
.hero-greet{width:292px;background:var(--red);color:var(--white);text-align:center;padding-top:26px}
.hero-greet h2{font-size:25px;font-weight:800}
.avatar{width:104px;height:104px;border-radius:50%;background:#f0d9c6;border:4px solid #fff;margin:14px auto 12px}
.hero-greet p{font-size:13px;font-weight:700;line-height:1.5;padding:0 40px}
.btn-dark{display:inline-block;background:var(--dark);color:#fff;font-weight:700;font-size:13px;padding:8px 18px;margin-top:12px}
.hero-photo{flex:1;position:relative;background:linear-gradient(90deg,#8a6a4a 0%,#c9a67d 30%,#efe9e2 55%,#4b4440 80%,#2b2624 100%)}
.hero-copy{position:absolute;left:465px;top:52px;color:#fff}
.hero-copy h1{font-size:33px;font-weight:800;line-height:1.1}
.hero-copy p{font-size:14px;font-weight:700;line-height:1.7;margin-top:10px}
.btn-red{display:inline-block;background:var(--red);color:#fff;font-weight:700;font-size:13px;padding:7px 14px;margin-top:18px}

.offer{margin:37px 92px 0;height:86px;display:flex}
.offer-title{width:292px;background:var(--red);color:#fff;font-size:32px;font-weight:800;display:flex;align-items:center;justify-content:center}
.offer-form{flex:1;background:var(--dark);color:#fff;text-align:center;padding-top:14px}
.offer-form p{font-size:13px;font-weight:700}
.fields{display:flex;justify-content:center;gap:3px;margin-top:8px}
.fields span{background:#fff;color:var(--muted);font-size:10px;width:138px;height:30px;line-height:30px}
.offer-btn{width:143px;background:var(--red);color:#fff;font-weight:800;font-size:15px;display:flex;align-items:center;justify-content:center}

.content{display:flex;gap:41px;margin:37px 92px 0}
.sidebar{width:292px}
.main{width:680px}

.box-head{height:34px;background:var(--red);color:#fff;font-weight:700;font-size:13px;display:flex;align-items:center;justify-content:space-between;padding-left:12px}
.plus{width:34px;height:34px;background:var(--dark);display:flex;align-items:center;justify-content:center;font-size:22px;font-weight:400}

.categories{list-style:none;padding:8px 0 20px}
.categories li{display:flex;align-items:center;gap:18px;padding:0 20px;height:38px;border-bottom:1px dashed var(--line);font-size:11px;font-weight:600}
.categories li:last-child{border:0}
.categories .sq{width:18px;height:18px;background:var(--btn);color:#fff;font-size:14px;display:flex;align-items:center;justify-content:center}
.categories li.active{color:var(--red)}
.categories li.active .sq{background:var(--red)}

.reasons{list-style:none;padding:16px 0 18px}
.reasons li{display:flex;gap:16px;padding:12px 0 14px 22px;border-bottom:1px dashed var(--line);height:117px}
.reasons li:last-child{border:0}
.num{width:30px;height:30px;background:var(--btn);color:#fff;font-weight:700;font-size:12px;display:flex;align-items:center;justify-content:center;flex:none}
.reasons li:first-child .num{background:var(--red)}
.item-title{color:var(--red);font-size:11px;font-weight:700}
.item-meta{color:var(--muted);font-size:7px;margin:2px 0 6px}
.item-text{color:var(--muted);font-size:10px;line-height:1.5}

.tabs{display:flex;align-items:center;height:34px;background:var(--red);color:#fff;font-weight:700;font-size:13px}
.tabs .tab{padding:0 12px;height:34px;display:flex;align-items:center}
.tabs .tab.soft{background:#c2bfb9;color:#fff;padding:0 8px}
.tabs .tab.gray{background:#9d9a95;padding:0 8px}
.tabs .plus{margin-left:auto}
.posts{list-style:none;padding:16px 0 8px}
.posts li{display:flex;gap:16px;padding:0 0 20px 22px;height:125px}
.date{flex:none;width:34px}
.date b{display:block;height:30px;background:var(--red);color:#fff;text-align:center;line-height:30px}
.date i{display:block;height:30px;background:var(--btn);color:#fff;text-align:center;line-height:30px;font-style:normal;font-weight:700}

.quotes{list-style:none;padding:22px 0 0}
.quotes li{display:flex;gap:18px;padding-bottom:20px;margin-bottom:22px;border-bottom:1px dashed var(--line)}
.quotes li:last-child{border:0}
.portrait{width:64px;height:74px;flex:none;background:linear-gradient(#8f7f76,#b7a69a)}
.quotes .who{font-size:11px;font-weight:700;color:#2a9fa0;margin-top:14px}
.quotes .who span{color:var(--text)}
.quotes .item-text{margin-top:4px}

.sec-head{display:flex;align-items:center;height:34px}
.sec-head h3{background:var(--red);color:#fff;font-size:13px;font-weight:700;height:34px;line-height:34px;padding:0 14px;border:2px solid var(--red)}
.sec-head .rule{flex:1;height:1px;background:var(--line)}
.arrows{display:flex;gap:2px}
.arrows span{width:28px;height:34px;background:var(--dark);color:#fff;display:flex;align-items:center;justify-content:center}
.viewall{background:var(--dark);color:#fff;font-weight:700;font-size:12px;height:34px;line-height:34px;padding:0 14px}

.grid{display:grid;grid-template-columns:repeat(3,1fr);column-gap:0}
.card{text-align:center;position:relative;padding-top:50px}
.card .pic{width:152px;height:142px;margin:0 auto;}
.badge{position:absolute;top:28px;right:52px;width:38px;height:38px;border-radius:50%;background:var(--orange);color:#fff;font-weight:800;font-size:11px;display:flex;align-items:center;justify-content:center}
.stars{color:var(--star);font-size:11px;letter-spacing:2px;margin-top:14px}
.stars em{color:#ccc;font-style:normal}
.card h4{font-size:11px;font-weight:700;margin-top:4px}
.card p{font-size:10px;color:#555;line-height:1.4;margin-top:2px}
.price{color:var(--red);font-weight:800;font-size:14px;margin-top:4px}
.buy{display:inline-flex;margin-top:10px;height:28px}
.buy span{background:var(--btn);color:#fff;font-size:10px;line-height:28px;padding:0 12px}
.buy i{width:30px;background:var(--red);display:flex;align-items:center;justify-content:center}

.sec-new .grid{height:348px}
.sec-best{margin-top:30px}
.sec-best .grid{height:350px}
.sec-feat{margin-top:30px}
.sec-feat .grid{row-gap:0}
.sec-feat .card{height:370px}

.features{position:absolute;left:0;top:2240px;width:1200px;height:366px;background:var(--dark);display:flex;justify-content:center;gap:9px;padding-left:4px}
.feature{width:330px;background:var(--mid);text-align:center;color:#fff}
.feature-head{height:97px;background:var(--red);display:flex;align-items:center;justify-content:center;gap:18px;font-size:21px;font-weight:800}
.dash{width:40px;height:2px;background:#aaa;margin:30px auto 16px}
.feature p{font-size:12px;line-height:1.55;padding:0 44px}
.cards{display:flex;justify-content:center;gap:10px;margin-top:18px}
.cards span{width:52px;height:30px;background:#fff;border-radius:3px}
.btn-outline{display:inline-block;border:2px solid #aaa;color:#ddd;font-weight:700;font-size:13px;letter-spacing:1px;padding:9px 30px;margin-top:22px}

.footer{position:absolute;left:0;top:2606px;width:1200px;height:88px;background:var(--darker);color:#ddd;display:flex;align-items:center;padding:0 95px;font-size:13px}
.footer b{color:#fff}
.footer nav{display:flex;gap:18px;margin-left:auto;margin-right:30px}
.social{display:flex;gap:8px}
.social span{width:26px;height:26px;border-radius:3px}
</style>
</head>
<body>

<div class="topbar">
  <span>Mirela, welcome to our online store!</span>
  <nav><a>Login</a><a>&#9679; My Account &#709;</a><a>&#9632; 0 item</a><a>Checkout</a></nav>
</div>

<header class="header">
  <div class="logo"><span class="logo-mark"></span>BRISANOVELTA</div>
  <nav class="mainnav">
    <a>HOME</a><a>SHOP BY BRAND</a><a>TOP SELLERS</a><a>CLEARANCE</a><a>HELP CENTER</a><a>MY FAVORITES</a><span class="sep"></span>
    <svg width="14" height="14" viewBox="0 0 14 14"><circle cx="6" cy="6" r="4.5" fill="none" stroke="#3b3735" stroke-width="2"/><line x1="9.5" y1="9.5" x2="13" y2="13" stroke="#3b3735" stroke-width="2"/></svg>
  </nav>
</header>

<section class="hero">
  <div class="hero-greet">
    <h2>HI MIRELA!</h2>
    <div class="avatar" role="img" aria-label="Illustrated avatar of the signed-in customer"></div>
    <p>accusantium laudantium unde perspiciatis ipsam sed</p>
    <a class="btn-dark">Learn more</a>
  </div>
  <div class="hero-photo" role="img" aria-label="Photo of a bedroom with a wooden wall, bed and bedside lamps">
    <div class="hero-copy">
      <h1>ACCUSANTI<br>LAUDANTIUM</h1>
      <p>PERSPICIATIS DOLORE TOTAM<br>UNDE UNDE ET AUT ILLO AUT</p>
      <a class="btn-red">pre-order now</a>
    </div>
  </div>
</section>

<section class="offer">
  <div class="offer-title">BEST OFFER</div>
  <div class="offer-form">
    <p>get your voucer TODAY and enter your email address below</p>
    <div class="fields"><span>your name</span><span>address</span><span>type your email here</span></div>
  </div>
  <a class="offer-btn">SUBSCRIBE</a>
</section>

<div class="content">
  <aside class="sidebar">
    <div class="box-head">SHOP BY CATEGORY<span class="plus">+</span></div>
    <ul class="categories">
      <li class="active"><span class="sq">+</span>VINTAGE FURNITURE</li>
      <li><span class="sq">+</span>RATTAN SET OUTDOOR AND INDOOR</li>
      <li><span class="sq">+</span>LAMPS AND</li>
      <li><span class="sq">+</span>WOODEN WALL DECOR</li>
    </ul>

    <div class="box-head">WHY YOU CHOOSE US<span class="plus">+</span></div>
    <ul class="reasons">
      <li><span class="num">01</span><div><div class="item-title">PERSPICIATIS IPSAM</div><div class="item-meta">Voluptatem, Totam</div><div class="item-text">Enim accusantium illum laudantium laudantium perspiciatis ipsam sed doloremque ipsam totam unde</div></div></li>
      <li><span class="num">02</span><div><div class="item-title">PERSPICIATIS IPSAM</div><div class="item-meta">Voluptatem, Totam</div><div class="item-text">Enim accusantium illum laudantium laudantium perspiciatis ipsam sed doloremque ipsam totam unde</div></div></li>
      <li><span class="num">03</span><div><div class="item-title">PERSPICIATIS IPSAM</div><div class="item-meta">Voluptatem, Totam</div><div class="item-text">Enim accusantium illum laudantium laudantium perspiciatis ipsam sed doloremque ipsam totam unde</div></div></li>
      <li><span class="num">04</span><div><div class="item-title">PERSPICIATIS IPSAM</div><div class="item-meta">Voluptatem, Totam</div><div class="item-text">Enim accusantium illum laudantium laudantium perspiciatis ipsam sed doloremque ipsam totam unde</div></div></li>
      <li><span class="num">05</span><div><div class="item-title">PERSPICIATIS IPSAM</div><div class="item-meta">Voluptatem, Totam</div><div class="item-text">Enim accusantium illum laudantium laudantium perspiciatis ipsam sed doloremque ipsam totam unde</div></div></li>
    </ul>

    <div class="tabs"><span class="tab">NEWS FROM BLOG</span><span class="tab soft">ENU 2</span><span class="tab gray">NU 3</span><span class="plus">+</span></div>
    <ul class="posts">
      <li><span class="date"><b>10</b><i>11</i></span><div><div class="item-title">VERITATIS BEATAE EOS</div><div class="item-meta">Voluptatem, Totam</div><div class="item-text">Accusantium laudantium laudantium perspiciatis ipsam sed doloremque ipsam totam unde accusantium</div></div></li>
      <li><span class="date"><b>10</b><i>11</i></span><div><div class="item-title">TOTAK UNDE</div><div class="item-meta">Voluptatem, Totam</div><div class="item-text">Accusantium laudantium laudantium perspiciatis ipsam sed doloremque ipsam totam unde accusantium</div></div></li>
      <li><span class="date"><b>10</b><i>11</i></span><div><div class="item-title">TOTAK UNDE</div><div class="item-meta">Voluptatem, Totam</div><div class="item-text">Accusantium laudantium laudantium perspiciatis ipsam sed doloremque ipsam totam unde accusantium</div></div></li>
    </ul>

    <div class="box-head">WHAT CUSTOMERS SAY<span class="plus">+</span></div>
    <ul class="quotes">
      <li><div class="portrait" role="img" aria-label="Portrait photo of a customer"></div><div><div class="who">TOMAS REYL <span>- MANAGER</span></div><div class="item-text">Enim accusantium illum laudae tumperspiciatis ipsam sed doloremque ipsam totam unde</div></div></li>
      <li><div class="portrait" role="img" aria-label="Portrait photo of a customer"></div><div><div class="who">TOMAS REYL <span>- MANAGER</span></div><div class="item-text">Enim accusantium illum laudae tumperspiciatis ipsam sed doloremque ipsam totam unde</div></div></li>
    </ul>
  </aside>

  <main class="main">
    <section class="sec-new">
      <div class="sec-head"><h3>NEW PRODUCTS OF THE WEEK</h3><span class="rule"></span><div class="arrows"><span>&#8249;</span><span>&#8250;</span></div></div>
      <div class="grid">
        <article class="card"><span class="badge">NEW</span><div class="pic" role="img" aria-label="Painted vintage chest of drawers" style="background:linear-gradient(135deg,#8a3a2c,#c95a48,#4e7f8f)"></div><div class="stars">★★★★<em>★</em></div><h4>REM IPSAM QUAS</h4><p>Enim accusantium laudantium<br>perspiciatis doloremque</p><div class="price">$ 987.00</div><div class="buy"><span>BUY NOW</span><i><svg width="14" height="12" viewBox="0 0 14 12"><path d="M0 1h3l2 7h7l2-5H4" fill="none" stroke="#fff" stroke-width="1.5"/><circle cx="6" cy="10.5" r="1.2" fill="#fff"/><circle cx="11" cy="10.5" r="1.2" fill="#fff"/></svg></i></div></article>
        <article class="card"><span class="badge">NEW</span><div class="pic" role="img" aria-label="Weathered wooden side table" style="background:linear-gradient(180deg,#fff 25%,#7fa9a8 40%,#8a6a4c 55%,#fff 100%)"></div><div class="stars">★★★★<em>★</em></div><h4>REM IPSAM QUAS</h4><p>Enim accusantium laudantium<br>perspiciatis doloremque</p><div class="price">$ 987.00</div><div class="buy"><span>BUY NOW</span><i><svg width="14" height="12" viewBox="0 0 14 12"><path d="M0 1h3l2 7h7l2-5H4" fill="none" stroke="#fff" stroke-width="1.5"/><circle cx="6" cy="10.5" r="1.2" fill="#fff"/><circle cx="11" cy="10.5" r="1.2" fill="#fff"/></svg></i></div></article>
        <article class="card"><span class="badge">NEW</span><div class="pic" role="img" aria-label="Reclaimed wood storage chest" style="background:linear-gradient(180deg,#fff 15%,#a88a66 30%,#7b8d7a 60%,#fff 90%)"></div><div class="stars">★★★★<em>★</em></div><h4>REM IPSAM QUAS</h4><p>Enim accusantium laudantium<br>perspiciatis doloremque</p><div class="price">$ 987.00</div><div class="buy"><span>BUY NOW</span><i><svg width="14" height="12" viewBox="0 0 14 12"><path d="M0 1h3l2 7h7l2-5H4" fill="none" stroke="#fff" stroke-width="1.5"/><circle cx="6" cy="10.5" r="1.2" fill="#fff"/><circle cx="11" cy="10.5" r="1.2" fill="#fff"/></svg></i></div></article>
      </div>
    </section>

    <section class="sec-best">
      <div class="sec-head"><h3>BESTSELLER PRODUCTS</h3><span class="rule"></span><div class="arrows"><span>&#8249;</span><span>&#8250;</span></div></div>
      <div class="grid">
        <article class="card"><span class="badge">50%</span><div class="pic" role="img" aria-label="Round rattan dining set" style="background:radial-gradient(ellipse at center,#4a4643 40%,#fff 72%)"></div><div class="stars">★★★★<em>★</em></div><h4>REM IPSAM QUAS</h4><p>Enim accusantium laudantium<br>perspiciatis doloremque</p><div class="price">$ 987.00</div><div class="buy"><span>BUY NOW</span><i><svg width="14" height="12" viewBox="0 0 14 12"><path d="M0 1h3l2 7h7l2-5H4" fill="none" stroke="#fff" stroke-width="1.5"/><circle cx="6" cy="10.5" r="1.2" fill="#fff"/><circle cx="11" cy="10.5" r="1.2" fill="#fff"/></svg></i></div></article>
        <article class="card"><span class="badge">20%</span><div class="pic" role="img" aria-label="Brass floor lamp with cream shade" style="background:radial-gradient(ellipse at 50% 20%,#f1d9a8 25%,#fff 60%)"></div><div class="stars">★★★★<em>★</em></div><h4>REM IPSAM QUAS</h4><p>Enim accusantium laudantium<br>perspiciatis doloremque</p><div class="price">$ 987.00</div><div class="buy"><span>BUY NOW</span><i><svg width="14" height="12" viewBox="0 0 14 12"><path d="M0 1h3l2 7h7l2-5H4" fill="none" stroke="#fff" stroke-width="1.5"/><circle cx="6" cy="10.5" r="1.2" fill="#fff"/><circle cx="11" cy="10.5" r="1.2" fill="#fff"/></svg></i></div></article>
        <article class="card"><div class="pic" role="img" aria-label="Round rattan lounge set" style="background:radial-gradient(ellipse at center,#b07a54 40%,#fff 72%)"></div><div class="stars">★★★★<em>★</em></div><h4>REM IPSAM QUAS</h4><p>Enim accusantium laudantium<br>perspiciatis doloremque</p><div class="price">$ 987.00</div><div class="buy"><span>BUY NOW</span><i><svg width="14" height="12" viewBox="0 0 14 12"><path d="M0 1h3l2 7h7l2-5H4" fill="none" stroke="#fff" stroke-width="1.5"/><circle cx="6" cy="10.5" r="1.2" fill="#fff"/><circle cx="11" cy="10.5" r="1.2" fill="#fff"/></svg></i></div></article>
      </div>
    </section>

    <section class="sec-feat">
      <div class="sec-head"><h3>FEATURED PRODUCTS</h3><span class="rule"></span><a class="viewall">view all</a></div>
      <div class="grid">
        <article class="card"><div class="pic" role="img" aria-label="Painted wooden cabinet with open door" style="background:linear-gradient(135deg,#7a5038,#b06a4c,#5c7f92)"></div><div class="stars">★★★★<em>★</em></div><h4>REM IPSAM QUAS</h4><p>Enim accusantium laudantium<br>perspiciatis doloremque</p><div class="price">$ 987.00</div><div class="buy"><span>BUY NOW</span><i><svg width="14" height="12" viewBox="0 0 14 12"><path d="M0 1h3l2 7h7l2-5H4" fill="none" stroke="#fff" stroke-width="1.5"/><circle cx="6" cy="10.5" r="1.2" fill="#fff"/><circle cx="11" cy="10.5" r="1.2" fill="#fff"/></svg></i></div></article>
        <article class="card"><div class="pic" role="img" aria-label="Painted vintage chest of drawers" style="background:linear-gradient(135deg,#8a3a2c,#c95a48,#4e7f8f)"></div><div class="stars">★★★★<em>★</em></div><h4>REM IPSAM QUAS</h4><p>Enim accusantium laudantium<br>perspiciatis doloremque</p><div class="price">$ 987.00</div><div class="buy"><span>BUY NOW</span><i><svg width="14" height="12" viewBox="0 0 14 12"><path d="M0 1h3l2 7h7l2-5H4" fill="none" stroke="#fff" stroke-width="1.5"/><circle cx="6" cy="10.5" r="1.2" fill="#fff"/><circle cx="11" cy="10.5" r="1.2" fill="#fff"/></svg></i></div></article>
        <article class="card"><div class="pic" role="img" aria-label="Tall reclaimed wood display cabinet" style="background:linear-gradient(90deg,#fff 25%,#8a6a3e 35%,#6f8a5a 65%,#fff 75%)"></div><div class="stars">★★★★<em>★</em></div><h4>REM IPSAM QUAS</h4><p>Enim accusantium laudantium<br>perspiciatis doloremque</p><div class="price">$ 987.00</div><div class="buy"><span>BUY NOW</span><i><svg width="14" height="12" viewBox="0 0 14 12"><path d="M0 1h3l2 7h7l2-5H4" fill="none" stroke="#fff" stroke-width="1.5"/><circle cx="6" cy="10.5" r="1.2" fill="#fff"/><circle cx="11" cy="10.5" r="1.2" fill="#fff"/></svg></i></div></article>
        <article class="card"><div class="pic" role="img" aria-label="Round rattan lounge set" style="background:radial-gradient(ellipse at center,#b07a54 40%,#fff 72%)"></div><div class="stars">★★★★<em>★</em></div><h4>REM IPSAM QUAS</h4><p>Enim accusantium laudantium<br>perspiciatis doloremque</p><div class="price">$ 987.00</div><div class="buy"><span>BUY NOW</span><i><svg width="14" height="12" viewBox="0 0 14 12"><path d="M0 1h3l2 7h7l2-5H4" fill="none" stroke="#fff" stroke-width="1.5"/><circle cx="6" cy="10.5" r="1.2" fill="#fff"/><circle cx="11" cy="10.5" r="1.2" fill="#fff"/></svg></i></div></article>
        <article class="card"><div class="pic" role="img" aria-label="Reclaimed wood storage chest" style="background:linear-gradient(180deg,#fff 15%,#a88a66 30%,#7b8d7a 60%,#fff 90%)"></div><div class="stars">★★★★<em>★</em></div><h4>REM IPSAM QUAS</h4><p>Enim accusantium laudantium<br>perspiciatis doloremque</p><div class="price">$ 987.00</div><div class="buy"><span>BUY NOW</span><i><svg width="14" height="12" viewBox="0 0 14 12"><path d="M0 1h3l2 7h7l2-5H4" fill="none" stroke="#fff" stroke-width="1.5"/><circle cx="6" cy="10.5" r="1.2" fill="#fff"/><circle cx="11" cy="10.5" r="1.2" fill="#fff"/></svg></i></div></article>
        <article class="card"><div class="pic" role="img" aria-label="Round rattan dining set" style="background:radial-gradient(ellipse at center,#4a4643 40%,#fff 72%)"></div><div class="stars">★★★★<em>★</em></div><h4>REM IPSAM QUAS</h4><p>Enim accusantium laudantium<br>perspiciatis doloremque</p><div class="price">$ 987.00</div><div class="buy"><span>BUY NOW</span><i><svg width="14" height="12" viewBox="0 0 14 12"><path d="M0 1h3l2 7h7l2-5H4" fill="none" stroke="#fff" stroke-width="1.5"/><circle cx="6" cy="10.5" r="1.2" fill="#fff"/><circle cx="11" cy="10.5" r="1.2" fill="#fff"/></svg></i></div></article>
      </div>
    </section>
  </main>
</div>

<section class="features">
  <div class="feature">
    <div class="feature-head"><svg width="30" height="28" viewBox="0 0 30 28"><rect x="2" y="4" width="22" height="18" fill="#fff"/><rect x="8" y="8" width="20" height="16" fill="none" stroke="#fff" stroke-width="2"/><rect x="2" y="9" width="22" height="3" fill="#d13a30"/></svg>PAYMENT METHOD</div>
    <div class="dash"></div>
    <p>Lorem ipsum dolor sit amet omnis aperiam</p>
    <div class="cards"><span></span><span></span><span></span><span></span></div>
    <a class="btn-outline">READ MORE</a>
  </div>
  <div class="feature">
    <div class="feature-head"><svg width="40" height="26" viewBox="0 0 40 26"><rect x="0" y="2" width="24" height="16" fill="#fff"/><path d="M24 7h8l6 6v5H24z" fill="#fff"/><circle cx="8" cy="21" r="4" fill="#fff"/><circle cx="31" cy="21" r="4" fill="#fff"/></svg>FREE SHIPPING</div>
    <div class="dash"></div>
    <p>Lorem ipsum dolor sit amet omnis aperiam ab ipsam ipsa odit aut aperiam apertur veritatis unde enim accusantium laudantium</p>
    <a class="btn-outline">READ MORE</a>
  </div>
  <div class="feature">
    <div class="feature-head"><svg width="26" height="26" viewBox="0 0 26 26"><circle cx="11" cy="11" r="8" fill="none" stroke="#fff" stroke-width="3"/><line x1="17" y1="17" x2="24" y2="24" stroke="#fff" stroke-width="3.5"/></svg>TRACK YOUR ORDER</div>
    <div class="dash"></div>
    <p>Lorem ipsum dolor sit amet omnis aperiam ab ipsam ipsa odit aut aperiam apertur veritatis unde enim accusantium laudantium</p>
    <a class="btn-outline">READ MORE</a>
  </div>
</section>

<footer class="footer">
  <span>© 2014 <b>YOUR COMPANY</b>. ALL RIGHTS RESERVED.</span>
  <nav><a>ABOUT US</a><a>TERM AND USE</a><a>PRIVACY POLICY</a><a>FAQS</a><a>CONTACT US</a></nav>
  <div class="social"><span style="background:#3b5998"></span><span style="background:#29a9e1"></span><span style="background:#d13a30"></span><span style="background:#1b86bd"></span><span style="background:#c8232c"></span></div>
</footer>

</body>
</html>
```